Collectibles expert needs a new business card design.

My current business card makes me look to high end. It may even make me look arrogant or too stuffy. I do work with high end clients and their items but most of my business is with average people with average items. My business name is Walter Brennick's Oak Lane Digging Co. The idea was that I mine the streets helping people discover the treasures buried in their homes. That could be art, jewelry, coins, etc. The name and an older logo I used does not make immediate sense to most people. I tried to go with just my picture and name and that is the current card I am changing. I help people who need to downsize. Whether they are getting rid of one item, a collection or a house full of items I help them discover what they have, what it is worth and what are the best ways we can get the most for them. This may be a combination of estate sale (which I dont do) auction or sell directly to a dealer or collector. Usually it is a combination of these. My main goal is to help make sure they dont accidently sell a Vantorre painting in a garage sale. I am uploading a copy of my old card and the old logo I used to use but the winning card design will need to be much different than these. You can learn a little more about me at www.walterpbrennick.com, www.oaklanedigin.com and www.facebook.com/oldco. I hope someone can look at what I do and come up with a very unique design that will be equally effective if my client is high income or if my client is low to mid income. I do not care if it is a one or two sided card as long as it conveys my contact information and a good representation of what I do.

Target Market(s)

People who are getting rid of items. These can be elderly couples or individuals that are moving to an active living community and will have less space so they need to sell items. This can also include the children of elder parents that dont want their stuff and want to find solutions to help them get rid of their items.

Contact Information for Business Card

The card should have my business name Walter Brennick's Oak Lane Digging Co., phone number 555-382-19073, email walter@oaklanedigging.com and website www.oaklanedigging.com. Would also like to include Buyer, Broker, Consultant and Appraiser. We can put Walter P. Brennick, ISA on the opposite side of the company name since it includes my name as well.

Font styles to use
Sans Serif

Colors

Designer to choose colors to be used in the design.

Requirements
Must have
• My project must have a professional look. It must not alienate low income clients and should still be appealing to high value clients.

```html
<!DOCTYPE html>
<html lang="en">
<head>
<meta charset="utf-8">
<title>Oak Lane Digging Co. — Business Card</title>
<link rel="stylesheet" href="https://fonts.googleapis.com/css2?family=Montserrat:wght@400;600&display=swap">
<style>
  :root {
    --backdrop: #eeebe6;
    --ink: #2e2822;
    --cream-text: #f1e8d8;
    --soft-text: #e2d6c2;
    --stone-light: #f6f1e9;
    --stone-mid: #e6dccd;
    --stone-vein: #cdbfa9;
  }
  * { margin: 0; padding: 0; box-sizing: border-box; }
  html, body { width: 1200px; height: 1200px; overflow: hidden; }
  body { background: var(--backdrop); position: relative; }

  .card {
    position: absolute;
    left: 228px;
    width: 746px;
    height: 416px;
    overflow: hidden;
    box-shadow: 0 6px 18px rgba(60,45,30,0.14);
  }
  .card--front { top: 148px; }
  .card--back { top: 637px; }

  .stone {
    position: absolute;
    background:
      linear-gradient(125deg, transparent 0 18%, rgba(205,191,169,0.55) 22%, transparent 30%),
      linear-gradient(150deg, transparent 0 55%, rgba(205,191,169,0.5) 60%, transparent 68%),
      linear-gradient(110deg, var(--stone-light) 0%, var(--stone-mid) 35%, var(--stone-light) 55%, var(--stone-vein) 75%, var(--stone-light) 100%);
  }
  .card--front .stone { inset: 0; }
  .card--back .stone { left: 0; top: 0; width: 226px; height: 100%; }

  .name-band {
    position: absolute;
    left: 0;
    top: 106px;
    width: 658px;
    height: 200px;
    background: var(--ink);
  }
  .name-band__name {
    position: absolute;
    left: 48px;
    top: 54px;
    font: 600 35px/1 "Montserrat", sans-serif;
    letter-spacing: 1.5px;
    color: var(--cream-text);
    white-space: nowrap;
  }
  .name-band__roles {
    position: absolute;
    left: 48px;
    top: 124px;
    font: 600 18px/1 "Montserrat", sans-serif;
    letter-spacing: 0.6px;
    color: var(--soft-text);
    white-space: nowrap;
  }

  .contact-panel {
    position: absolute;
    left: 226px;
    top: 0;
    right: 0;
    bottom: 0;
    background: var(--ink);
  }
  .company {
    position: absolute;
    left: 60px;
    top: 100px;
    font: 600 26px/1.35 "Montserrat", sans-serif;
    letter-spacing: 1.4px;
    color: var(--cream-text);
    white-space: nowrap;
  }
  .contact-list {
    position: absolute;
    left: 60px;
    top: 244px;
    list-style: none;
    font: 400 16px/27px "Montserrat", sans-serif;
    letter-spacing: 1px;
    color: var(--soft-text);
    white-space: nowrap;
  }
</style>
</head>
<body>
  <section class="card card--front">
    <div class="stone" role="img" aria-label="Warm cream stone texture"></div>
    <div class="name-band">
      <h1 class="name-band__name">WALTER P. BRENNICK, ISA</h1>
      <p class="name-band__roles">BUYER, BROKER, CONSULTANT AND APPRAISER</p>
    </div>
  </section>

  <section class="card card--back">
    <div class="stone" role="img" aria-label="Warm cream stone texture"></div>
    <div class="contact-panel">
      <h2 class="company">WALTER BRENNICK'S<br>OAK LANE DIGGING CO.</h2>
      <ul class="contact-list">
        <li>555-382-19073</li>
        <li>walter@oaklanedigging.com</li>
        <li>www.oaklanedigging.com</li>
      </ul>
    </div>
  </section>
</body>
</html>
```